Trifold Brochure for Velmora Skincare Clinic

We want to have a brochure to reach out to the potential clients and tell them who we are and what service we provide. Equipped with the latest laser technology and medical grade products, we have a derm doctor and experienced cosmetic clinician/educator in place to serve each client's individual skin care needs at the highest quality at a reasonable price. We had two previous designs failed to meet our expectation for the artistry and content to match the level of our service quality. We post the two previous design here, in hope we can find a quality design to serve our purpose. You can use the content in our uploaded word file. Or you can delete the "Velmora Specials" including the listing price part in the left column on the cover page. Please be noted that we want the BIOs in the VSC_Brochure-Carstairs-09-03-19.pdf file (the middle column on the cover page)

I have attached sample look and feel in a word file. Hope the results can be better.

File 5 and File 6 are logo.

We are thinking about A4 size paper.

Target Market(s)

Our clients are middle aged woman and man.

Colors
eea4c8

Requirements
Must have
• Velmora Logo (file 5), Velmora watermark(file 6), elegant and feminine figures, colors, organic shapes and lines; sense of quality and understated luxury, emphasizing on style and sophistication
• multi colors, must including the pink color in the following color pick
Nice to have
• incorporate something like femaleOutline.jpeg (file 7). But note that we don't have copy right to this picture.

```html
<!DOCTYPE html>
<html lang="en">
<head>
<meta charset="utf-8">
<title>Velmora Skin Care – Trifold Brochure</title>
<link href="https://fonts.googleapis.com/css2?family=Open+Sans:wght@400;600;700&family=Russo+One&family=Poiret+One&display=swap" rel="stylesheet">
<style>
  :root{
    --page:#ffffff;
    --band-grey:#6e6d71;
    --pink-soft:#f7c6ef;
    --pink-light:#fbe3f7;
    --magenta:#ef3fe6;
    --magenta-deep:#d82fd0;
    --ink:#1c1c1c;
    --body:#333333;
    --white:#ffffff;
    --splash:#f4c8d8;
  }
  *{margin:0;padding:0;box-sizing:border-box}
  html,body{width:1200px;height:1000px;overflow:hidden;background:var(--page)}
  body{position:relative;font-family:"Open Sans",sans-serif;color:var(--body)}

  .brochure{position:absolute;left:0;top:76px;width:1200px;height:846px}

  .inner-panels{
    position:absolute;left:0;top:0;width:800px;height:846px;
    background:
      radial-gradient(circle at 15% 55%, rgba(255,255,255,.7) 0 60px, transparent 120px),
      radial-gradient(circle at 60% 40%, rgba(255,255,255,.6) 0 80px, transparent 160px),
      radial-gradient(circle at 90% 75%, rgba(255,255,255,.5) 0 70px, transparent 150px),
      linear-gradient(180deg,var(--pink-soft) 0%,var(--pink-light) 45%,var(--pink-soft) 100%);
  }
  .header-band{position:absolute;left:0;top:0;width:800px;height:150px}
  .band-title{
    position:absolute;font-family:"Russo One",sans-serif;color:var(--white);
    font-size:22px;line-height:30px;letter-spacing:.3px;
  }
  .band-title--left{left:40px;top:36px}
  .band-title--middle{left:440px;top:36px}

  .column{position:absolute;font-size:14.5px;line-height:20.5px;color:var(--body)}
  .column--left{left:40px;top:158px;width:320px}
  .column--middle{left:440px;top:155px;width:325px}

  .section-heading{font-weight:700;font-size:19px;line-height:24px;color:var(--ink);margin-bottom:6px}
  .section + .section{margin-top:14px}
  .price-list{list-style:none;margin:8px 0 0 29px;line-height:23.3px}
  .column--middle p + p{margin-top:12px}

  .contact-seal{position:absolute;left:465px;top:585px;width:230px;height:230px}
  .contact-seal__text{
    position:absolute;left:0;top:38px;width:230px;text-align:center;
    font-size:13.5px;line-height:17px;color:var(--ink);
  }
  .brand-name{font-family:"Open Sans",sans-serif;font-weight:400;color:#3a3a3a}
  .contact-seal .brand-name{display:block;font-size:25px;line-height:26px;margin-bottom:12px}
  .contact-seal .brand-name span{display:block;font-size:18px;line-height:20px;padding-left:40px}

  .cover{
    position:absolute;left:800px;top:0;width:400px;height:846px;
    background:linear-gradient(90deg,#f07ae8 0%,var(--magenta) 25%,var(--magenta) 85%,var(--magenta-deep) 100%);
    overflow:hidden;
  }
  .cover__splash{position:absolute;left:25px;top:40px;width:200px;height:150px;border-radius:40% 60% 55% 45%;
    background:radial-gradient(ellipse at 50% 50%,var(--splash) 0%,rgba(244,200,216,.6) 60%,transparent 75%)}
  .cover__brand{position:absolute;left:42px;top:92px;font-size:34px;line-height:34px}
  .cover__brand span{display:block;font-size:25px;line-height:30px;padding-left:70px}
  .cover__figure{position:absolute;left:270px;top:10px;width:120px;height:830px;
    background:linear-gradient(180deg,rgba(255,255,255,.18),rgba(255,255,255,.06));
    border-radius:60% 0 0 40%}
  .cover__tagline{position:absolute;left:45px;top:268px;width:220px;font-family:"Poiret One",sans-serif;
    font-size:27px;line-height:34px;color:var(--white);text-transform:uppercase}
  .cover__lead{position:absolute;left:43px;font-family:"Russo One",sans-serif;color:var(--white)}
  .cover__lead--first{top:448px;font-size:22px}
  .cover__lead--care{top:518px;font-size:26px}
  .cover__title{position:absolute;left:43px;top:600px;font-family:"Russo One",sans-serif;font-size:35px;line-height:46px;color:var(--white)}
  .cover__phone{position:absolute;left:43px;top:692px;font-family:"Russo One",sans-serif;font-size:20px;color:var(--ink)}
</style>
</head>
<body>
<main class="brochure">
  <section class="inner-panels">
    <svg class="header-band" viewBox="0 0 800 150" aria-hidden="true">
      <path d="M0 0H800V140C700 118 620 100 520 106C420 112 330 116 220 112C130 109 60 114 0 120Z" fill="var(--band-grey)"/>
      <path d="M0 120C60 114 130 109 220 112C330 116 420 112 520 106C620 100 700 118 800 140" fill="none" stroke="#ffffff" stroke-width="3"/>
      <path d="M0 128C80 120 160 118 260 122C360 126 450 118 540 114C640 110 720 128 800 148" fill="none" stroke="#f3a9e8" stroke-width="2"/>
    </svg>
    <h2 class="band-title band-title--left">VELMORA MEMBERSHIPS AND<br>PROMOTIONS/PACKAGES</h2>
    <h2 class="band-title band-title--middle">BETTER SKIN STARTS HERE</h2>

    <div class="column column--left">
      <div class="section">
        <h3 class="section-heading">LASER HAIR REMOVAL SERVICES</h3>
        <p>At Velmora patients can be treated virtually pain free with our advanced laser technology that will safely and effectively eliminate unwanted hair.</p>
        <ul class="price-list">
          <li>Lip / Chin - 50</li>
          <li>Underarm - 90</li>
          <li>Bikini - 100+</li>
          <li>Brazilian - 150+</li>
          <li>Neck – 70</li>
          <li>Full Leg 300</li>
          <li>Full Leg w/ bikini 350+</li>
          <li>Arms - 200+</li>
          <li>Back with Shoulders and neck 300+</li>
          <li>Chest – 200+</li>
        </ul>
      </div>
      <div class="section">
        <h3 class="section-heading">HEALTHY SKIN IS IMPORTANT<br>TO US</h3>
        <p>At Velmora we carry Medical Grade products for all of your skin care concerns with targeted active ingredients to smooth, refine and let your skin glow</p>
      </div>
      <div class="section">
        <h3 class="section-heading">DID YOU KNOW ...</h3>
        <p>Exclusive memberships and Packages are available. Completely tailored to your needs.</p>
        <p style="margin-top:14px">You can book your complimentary consult online at velmoraskincare.ca or via our social page @velmoraskincareca</p>
      </div>
    </div>

    <div class="column column--middle">
      <p>Dr. Harlan is a Redwater based family physician specializing in Dermatological Medical Procedures and Cosmetic Services. He has also served as a peer reviewer for scientific journals, such as the Journal of Aesthetic Skin Science. An avid watcher of ocean documentaries, Dr. Harlan loves hammerhead sharks.</p>
      <p>Corinne has over 15 years of clinical experience, as well as the past 8 years as a Clinical Educator and Director of Cosmetics Skin Education. Corinne was born and raised in the Linden Creek area and loves what she does: passionately working with patients to achieve their desired results.</p>
    </div>

    <div class="contact-seal">
      <svg width="230" height="230" viewBox="0 0 230 230" aria-hidden="true">
        <circle cx="115" cy="115" r="108" fill="#ffffff"/>
        <circle cx="115" cy="115" r="110" fill="none" stroke="var(--magenta)" stroke-width="3"/>
        <circle cx="117" cy="113" r="104" fill="none" stroke="#b83ab5" stroke-width="2"/>
        <circle cx="113" cy="117" r="113" fill="none" stroke="#9a2c9a" stroke-width="1.5"/>
      </svg>
      <div class="contact-seal__text">
        <span class="brand-name">Velmora<span>Skin Care</span></span>
        (555) 014-GLOW (4569)<br>
        info@velmoraskincare.ca<br>
        2240 Linden Street<br>
        Marlowe, MB, R2V 4K8
      </div>
    </div>
  </section>

  <section class="cover">
    <div class="cover__splash" role="img" aria-label="Soft pink brush splash behind the clinic name"></div>
    <div class="cover__brand brand-name">Velmora<span>Skin Care</span></div>
    <div class="cover__figure" role="img" aria-label="Line drawing of an elegant female silhouette in profile"></div>
    <p class="cover__tagline">Beauty and health at every stage of your life</p>
    <p class="cover__lead cover__lead--first">But First ...</p>
    <p class="cover__lead cover__lead--care">Skin Care</p>
    <h1 class="cover__title">COSMETIC<br>&amp; LASER</h1>
    <p class="cover__phone">555 -014-GLOW (4569)</p>
  </section>
</main>
</body>
</html>
```